Boat business cards

I'm looking for business cards with the two logos I've attached. I don't have an specific idea in mind and open to anything. All the usual info will be on the card. Name, position in company, nr, email, address, ect. The company rents out these two boats for charters and fishing.

```html
<!DOCTYPE html>
<html lang="en">
<head>
<meta charset="utf-8">
<title>Charter Captain Business Cards</title>
<link href="https://fonts.googleapis.com/css2?family=Montserrat:ital,wght@0,500;0,600;0,700;0,800;1,800&display=swap" rel="stylesheet">
<style>
  :root {
    --page: #ffffff;
    --card: #ffffff;
    --ink: #2a2a2a;
    --fleet-blue: #6b93c4;
    --fleet-brown: #8c6f4a;
    --rule: #8a8a8a;
    --sky: #dde7f2;
    --sea: #2f5fa6;
    --sea-deep: #1f4587;
  }
  * { margin: 0; padding: 0; box-sizing: border-box; }
  html, body {
    width: 1200px; height: 1200px; overflow: hidden;
    background: var(--page);
    font-family: "Montserrat", sans-serif;
    color: var(--ink);
  }
  .sheet { position: relative; width: 1200px; height: 1200px; }
  .card {
    position: absolute; left: 201px; width: 780px; height: 472px;
    background: var(--card); overflow: hidden;
    outline: 1px solid #ececec;
  }
  .card--front { top: 87px; }
  .card--back { top: 624px; }
  .card__splash { position: absolute; left: 0; top: 0; width: 780px; height: 472px; }

  .brand {
    position: absolute; display: flex; align-items: center; gap: 10px;
    font-weight: 700; font-size: 30px; letter-spacing: 0.5px; white-space: nowrap;
  }
  .brand__dot { width: 14px; height: 14px; border-radius: 50%; flex: none; }
  .brand--salt { color: #3a3a3a; }
  .brand--salt .brand__dot { background: var(--fleet-blue); }
  .brand--harbor { color: #111; }
  .brand--harbor .brand__dot { background: var(--fleet-brown); }

  .contact { position: absolute; width: 330px; }
  .contact--left { left: 76px; top: 312px; }
  .contact--right { left: 427px; top: 308px; }
  .contact__name { font-size: 21px; font-weight: 800; line-height: 1.1; }
  .contact--left .contact__name { color: var(--fleet-blue); font-style: italic; }
  .contact--right .contact__name { color: var(--fleet-brown); font-weight: 700; font-size: 24px; }
  .contact__role { margin-top: 8px; font-size: 11px; font-weight: 600; letter-spacing: 3px; }
  .contact--left .contact__role { font-weight: 800; font-style: italic; }
  .contact__service { margin-top: 18px; font-size: 13px; font-weight: 700; letter-spacing: 0.6px; }
  .contact--left .contact__service { color: var(--fleet-blue); }
  .contact--right .contact__service { color: var(--fleet-brown); }
  .contact__row { display: flex; align-items: center; gap: 18px; margin-top: 11px; font-size: 12.5px; font-weight: 500; white-space: nowrap; }
  .contact__item { display: flex; align-items: center; gap: 7px; }
  .contact__item svg { width: 12px; height: 12px; flex: none; }
  .contact--left svg { stroke: var(--fleet-blue); fill: none; }
  .contact--right svg { stroke: var(--fleet-brown); fill: none; }
  .contact__row--address { margin-top: 12px; }

  .back__divider { position: absolute; left: 374px; top: 248px; width: 1.5px; height: 137px; background: var(--rule); }
  .back__web { position: absolute; left: 0; width: 780px; top: 406px; text-align: center; font-size: 25px; font-weight: 600; letter-spacing: 0.5px; }
</style>
</head>
<body>
<main class="sheet">

  <section class="card card--front">
    <svg class="card__splash" viewBox="0 0 780 472" role="img" aria-label="Photo of a sport fishing boat on open blue sea beside a rocky headland">
      <defs>
        <linearGradient id="seaFront" x1="0" y1="0" x2="0" y2="1">
          <stop offset="0" stop-color="var(--sky)"/>
          <stop offset="0.42" stop-color="#c7d6ea"/>
          <stop offset="0.46" stop-color="var(--sea)"/>
          <stop offset="1" stop-color="var(--sea-deep)"/>
        </linearGradient>
      </defs>
      <path fill="url(#seaFront)" d="M148 0 H612 C606 20 628 40 640 62 C646 80 630 96 610 110 C590 122 560 118 540 140 C520 160 500 150 470 152 C450 150 440 160 430 168 C420 158 405 150 398 160 C390 172 385 180 378 198 C372 188 376 170 362 160 C340 150 320 150 300 138 C280 128 260 126 240 130 C220 132 210 120 205 110 C195 96 178 88 182 72 C186 58 160 50 152 38 C146 26 150 12 148 0 Z"/>
      <circle cx="620" cy="136" r="3" fill="var(--sea)"/>
      <circle cx="598" cy="132" r="2" fill="var(--sea)"/>
      <circle cx="175" cy="117" r="2" fill="var(--sea)"/>
    </svg>

    <div class="brand brand--salt" style="left:80px; top:236px;"><span class="brand__dot"></span>Salt Run</div>
    <div class="brand brand--harbor" style="left:428px; top:255px;"><span class="brand__dot"></span>Harbor Star</div>

    <div class="contact contact--left">
      <div class="contact__name">Rafael Ortega</div>
      <div class="contact__role">CAPTAIN</div>
      <div class="contact__service">CHARTERS AND FISHING</div>
      <div class="contact__row">
        <span class="contact__item"><svg viewBox="0 0 24 24" stroke-width="2.2"><path d="M5 3h4l2 5-3 2a12 12 0 0 0 6 6l2-3 5 2v4a2 2 0 0 1-2 2A17 17 0 0 1 3 5a2 2 0 0 1 2-2z"/></svg>123-456-789</span>
        <span class="contact__item"><svg viewBox="0 0 24 24" stroke-width="2"><circle cx="12" cy="12" r="9"/><path d="M3 12h18M12 3c3 3 3 15 0 18M12 3c-3 3-3 15 0 18"/></svg>www.loremipsum.com</span>
      </div>
      <div class="contact__row contact__row--address">
        <span class="contact__item"><svg viewBox="0 0 24 24" stroke-width="2.4"><path d="M12 22s-7-7-7-12a7 7 0 0 1 14 0c0 5-7 12-7 12z"/><circle cx="12" cy="10" r="2.5"/></svg>1234 Ocean Drive, Seaview, CA 54321</span>
      </div>
    </div>

    <div class="contact contact--right">
      <div class="contact__name">Daniel Whitaker</div>
      <div class="contact__role">CAPTAIN</div>
      <div class="contact__service">CHARTERS AND FISHING</div>
      <div class="contact__row">
        <span class="contact__item"><svg viewBox="0 0 24 24" stroke-width="2.2"><path d="M5 3h4l2 5-3 2a12 12 0 0 0 6 6l2-3 5 2v4a2 2 0 0 1-2 2A17 17 0 0 1 3 5a2 2 0 0 1 2-2z"/></svg>123-456-789</span>
        <span class="contact__item"><svg viewBox="0 0 24 24" stroke-width="2"><circle cx="12" cy="12" r="9"/><path d="M3 12h18M12 3c3 3 3 15 0 18M12 3c-3 3-3 15 0 18"/></svg>www.loremipsum.com</span>
      </div>
      <div class="contact__row contact__row--address">
        <span class="contact__item"><svg viewBox="0 0 24 24" stroke-width="2.4"><path d="M12 22s-7-7-7-12a7 7 0 0 1 14 0c0 5-7 12-7 12z"/><circle cx="12" cy="10" r="2.5"/></svg>1234 Ocean Drive, Seaview, CA 54321</span>
      </div>
    </div>
  </section>

  <section class="card card--back">
    <svg class="card__splash" viewBox="0 0 780 472" role="img" aria-label="Photo of a sport fishing boat on open blue sea beside a rocky headland">
      <defs>
        <linearGradient id="seaBack" x1="0" y1="0" x2="0" y2="1">
          <stop offset="0" stop-color="var(--sky)"/>
          <stop offset="0.5" stop-color="#c7d6ea"/>
          <stop offset="0.54" stop-color="var(--sea)"/>
          <stop offset="1" stop-color="var(--sea-deep)"/>
        </linearGradient>
      </defs>
      <path fill="url(#seaBack)" d="M30 0 H778 C772 30 760 60 740 80 C720 100 736 120 720 130 C700 140 680 120 670 140 C660 160 640 150 620 158 C596 168 580 176 560 168 C540 162 520 170 505 180 C490 194 475 200 470 220 C466 238 462 245 458 245 C454 235 455 210 445 195 C435 182 420 186 410 200 C398 212 395 190 380 186 C360 182 350 198 330 200 C305 204 290 200 275 210 C255 222 240 230 235 225 C226 214 220 200 205 196 C185 190 170 180 165 165 C160 150 138 142 130 120 C122 100 110 90 90 80 C70 70 62 50 55 35 C48 24 30 16 30 0 Z"/>
      <circle cx="740" cy="62" r="3" fill="#333"/>
      <circle cx="722" cy="82" r="2" fill="#333"/>
      <circle cx="252" cy="218" r="3" fill="var(--sea)"/>
      <circle cx="145" cy="196" r="2.5" fill="var(--sea)"/>
    </svg>

    <div class="brand brand--salt" style="left:98px; top:282px;"><span class="brand__dot"></span>Salt Run</div>
    <div class="back__divider"></div>
    <div class="brand brand--harbor" style="left:424px; top:302px;"><span class="brand__dot"></span>Harbor Star</div>

    <div class="back__web">www.loremipsum.com</div>
  </section>

</main>
</body>
</html>
```